HVAC company business card design

We need a business card design for a HVAC company. The design must look professional. Both sides will be used. The total data to be on the business card is
Name
Position
Email
Direct Phone/Moile Phone
Company Contacts /Address, Phone, Fax, web)
All data will be submit once the design is confirmed. For generic purposes use;
Cem Orkut
Managing Director
+902324418352 (Mobile)
4718 Sokak No: 9 KGTB Alsancak IZMIR TURKEY
Tel: +902324418352 Fax : +902324418359
www.ozkivra.com.tr

Target Market(s)

HVAC

Industry/Entity Type

Business

Contact Information for Business Card

The total data to be on the business card is
Name
Position
Email
Direct Phone/Moile Phone
Cem Orkut
Managing Director
+902324418352 (Mobile)
www.ozkivra.com.tr
The BC will use both sides of the card. The front will include the full logo and the details for the business card holder. The business card can be divided into vertical/horizontal or to a special shape. The common data like the company address/phone/fax should be indicated elsewehere. The back can contain some part or the whole logo and must contain the web address.

Font styles to use
Serif
Sans Serif

Colors
0355a3
cfdfed

Requirements
Should not have
• Please be careful with the fonts, it shouldnt be too small or too big and must not interfere with the logo fonts. If you need to use a curvy shape please do not use as the logo is already curvy or use the curves from the logo (if it looks good, otherwise forget it)
• We are not in favor of pictograms, only if they are perfect use them.

```html
<!DOCTYPE html>
<html lang="en">
<head>
<meta charset="utf-8">
<title>Ozkivra Business Card</title>
<link href="https://fonts.googleapis.com/css2?family=Questrial&display=swap" rel="stylesheet">
<style>
  :root {
    --stage: #d9dbdf;
    --card-cream: #f4f2e8;
    --card-navy: #3a4560;
    --brand-blue: #0355a3;
    --brand-light: #cfdfed;
    --ink: #2b2f38;
    --rule: #d6d3c4;
    --mark-light: #e4e9f1;
  }
  * { margin: 0; padding: 0; box-sizing: border-box; }
  html, body { width: 1200px; height: 786px; overflow: hidden; }
  body {
    background: var(--stage);
    font-family: "Questrial", "Century Gothic", sans-serif;
    color: var(--ink);
    position: relative;
  }
  .card {
    position: absolute;
    top: 238px;
    width: 480px;
    height: 310px;
    border-radius: 14px;
    overflow: hidden;
    box-shadow: 0 6px 18px rgba(0,0,0,0.18);
  }
  .card-front { left: 90px; background: var(--card-cream); }
  .card-back { left: 630px; background: var(--card-navy); }

  .front-swoosh { position: absolute; inset: 0; }

  .brand {
    position: absolute;
    display: flex;
    align-items: center;
    gap: 10px;
  }
  .brand-dot {
    border-radius: 50%;
    background: var(--brand-blue);
    flex: none;
  }
  .brand-name { letter-spacing: 2px; line-height: 1; }

  .card-front .brand { left: 34px; top: 96px; }
  .card-front .brand-dot { width: 34px; height: 34px; }
  .card-front .brand-name { font-size: 32px; color: var(--brand-blue); }

  .divider {
    position: absolute;
    left: 252px; top: 40px;
    width: 1px; height: 150px;
    background: var(--rule);
  }

  .holder {
    position: absolute;
    left: 268px; top: 34px;
    font-size: 11.5px;
    line-height: 1.55;
  }
  .holder-name {
    font-size: 14px;
    color: var(--brand-blue);
    text-transform: uppercase;
    letter-spacing: 0.5px;
  }
  .holder-title { margin-bottom: 6px; }
  .contact-list { list-style: none; }
  .contact-list li { display: flex; align-items: center; gap: 6px; }
  .contact-icon {
    width: 12px; height: 12px;
    border-radius: 2px;
    background: var(--brand-blue);
    flex: none;
  }
  .address { margin-top: 8px; }

  .card-back .brand { left: 50%; top: 50%; transform: translate(-50%, -50%); }
  .card-back .brand-dot { width: 44px; height: 44px; }
  .card-back .brand-name { font-size: 42px; color: var(--mark-light); }
</style>
</head>
<body>

<section class="card card-front" aria-label="Card front">
  <svg class="front-swoosh" width="480" height="310" viewBox="0 0 480 310" aria-hidden="true">
    <path d="M0 150 C 90 185, 200 215, 300 310" fill="none" stroke="var(--brand-blue)" stroke-width="6"/>
    <path d="M0 166 C 100 200, 190 240, 260 310" fill="none" stroke="var(--brand-light)" stroke-width="3"/>
  </svg>

  <div class="brand">
    <span class="brand-dot"></span>
    <span class="brand-name">OZKIVRA</span>
  </div>

  <div class="divider"></div>

  <div class="holder">
    <div class="holder-name">Cem Orkut</div>
    <div class="holder-title">Managing Director</div>
    <ul class="contact-list">
      <li>
        <svg class="contact-icon" viewBox="0 0 12 12" aria-label="Phone"><path d="M3 2.5 L5 4.5 L4 5.5 Q5 7.5 6.5 8 L7.5 7 L9.5 9 L8.5 10 Q4 9.5 2 4 Z" fill="#fff"/></svg>
        <span>+902324418352</span>
      </li>
      <li>
        <svg class="contact-icon" viewBox="0 0 12 12" aria-label="Fax"><rect x="3" y="2.5" width="6" height="3" fill="#fff"/><rect x="2" y="6" width="8" height="3.5" fill="#fff"/></svg>
        <span>+902324418359</span>
      </li>
      <li>
        <svg class="contact-icon" viewBox="0 0 12 12" aria-label="Mobile"><rect x="4" y="2" width="4" height="8" rx="0.8" fill="#fff"/></svg>
        <span>+902324418366</span>
      </li>
      <li>
        <svg class="contact-icon" viewBox="0 0 12 12" aria-label="Email"><rect x="2" y="3.5" width="8" height="5" fill="#fff"/><path d="M2 3.5 L6 6.5 L10 3.5" fill="none" stroke="var(--brand-blue)" stroke-width="0.8"/></svg>
        <span>info@ozkivra.com.tr</span>
      </li>
      <li>
        <svg class="contact-icon" viewBox="0 0 12 12" aria-label="Web"><circle cx="6" cy="6" r="3.6" fill="none" stroke="#fff" stroke-width="1"/><path d="M2.4 6 H9.6 M6 2.4 V9.6" stroke="#fff" stroke-width="0.8"/></svg>
        <span>www.ozkivra.com.tr</span>
      </li>
    </ul>
    <div class="address">
      4718 Sokak No: 9<br>
      KGTB Alsancak IZMIR TURKEY
    </div>
  </div>
</section>

<section class="card card-back" aria-label="Card back">
  <div class="brand">
    <span class="brand-dot"></span>
    <span class="brand-name">OZKIVRA</span>
  </div>
</section>

</body>
</html>
```